Business cards and stationery for medical company
Business cards, letter heads & envelopes
Professional
Dr.Felix Barsow
President and CEO
418 Tallowfield Lane
Northbrook, IL 60519 USA
fbarsow@curavista.us
www.curavista.us
Please use the 1-st option color on white background.

```html
<!DOCTYPE html>
<html lang="en">
<head>
<meta charset="utf-8">
<title>CuraVista Business Card</title>
<link href="https://fonts.googleapis.com/css2?family=Lato:wght@400;700&family=Cinzel:wght@400&display=swap" rel="stylesheet">
<style>
  :root{
    --stage:#e8e9eb;
    --card:#ffffff;
    --navy:#1d3c78;
    --blue:#2257a8;
    --sky:#4fa3e0;
    --red:#c8202f;
    --ink:#33415c;
  }
  *{margin:0;padding:0;box-sizing:border-box}
  html,body{width:1200px;height:799px;overflow:hidden}
  body{background:var(--stage);font-family:'Lato',sans-serif;position:relative}
  .card{position:absolute;width:540px;height:309px;background:var(--card);box-shadow:0 6px 18px rgba(0,0,0,.12);overflow:hidden}
  .card-back{left:40px;top:245px}
  .card-front{left:620px;top:245px}
  .brand{display:flex;align-items:center;gap:8px;font-family:'Lato',sans-serif;font-weight:700;color:var(--blue)}
  .brand-dot{width:12px;height:12px;border-radius:50%;background:var(--red)}
  .card-back .brand{position:absolute;left:0;right:0;top:118px;justify-content:center;font-size:40px}
  .card-back .web{position:absolute;right:34px;bottom:30px;color:var(--red);font-size:15px;font-weight:700}
  .card-front .brand{position:absolute;left:28px;top:44px;font-size:30px}
  .band{position:absolute;left:0;top:0;width:540px;height:309px}
  .holder{position:absolute;left:330px;top:26px;color:var(--navy)}
  .holder .name{font-family:'Cinzel',serif;font-size:19px}
  .holder .title{font-size:11px;margin-top:3px}
  .holder .addr{font-size:10.5px;margin-top:12px;line-height:1.45;color:var(--ink)}
  .contacts{position:absolute;left:330px;top:142px;list-style:none;font-size:10.5px;color:var(--ink)}
  .contacts li{display:flex;align-items:center;gap:6px;line-height:1.6}
  .contacts svg{width:11px;height:11px}
  .card-front .web{position:absolute;right:22px;bottom:20px;color:#fff;font-size:15px;font-weight:700}
</style>
</head>
<body>
  <section class="card card-back">
    <div class="brand"><span class="brand-dot"></span>CuraVista</div>
    <div class="web">www.curavista.us</div>
  </section>

  <section class="card card-front">
    <svg class="band" viewBox="0 0 540 309" aria-hidden="true">
      <defs>
        <linearGradient id="bandFill" x1="0" y1="0" x2="1" y2="0">
          <stop offset="0" stop-color="#1d3c78"/>
          <stop offset=".55" stop-color="#2a6fc0"/>
          <stop offset="1" stop-color="#4fa3e0"/>
        </linearGradient>
      </defs>
      <path d="M0 218 C150 205 300 222 540 258 L540 309 L0 309 Z" fill="url(#bandFill)"/>
      <path d="M0 238 C170 232 330 250 540 300 L540 309 L0 309 Z" fill="#1d3c78" opacity=".55"/>
      <path d="M0 206 C160 190 320 208 540 248" fill="none" stroke="#c8202f" stroke-width="3"/>
    </svg>
    <div class="brand"><span class="brand-dot"></span>CuraVista</div>
    <div class="holder">
      <div class="name">Dr.Felix Barsow</div>
      <div class="title">President &amp; CEO</div>
      <div class="addr">418 Tallowfield Lane<br>Northbrook, IL 60519 USA</div>
    </div>
    <ul class="contacts">
      <li><svg viewBox="0 0 12 12"><circle cx="6" cy="6" r="5.3" fill="none" stroke="#1d3c78"/><path d="M4 3.5l1 1-.6.8c.4.9 1 1.5 1.8 1.9l.8-.6 1 1-.7.9C5.5 8.3 3.7 6.5 3.3 4.3z" fill="#1d3c78"/></svg>(847) 555-0142</li>
      <li><svg viewBox="0 0 12 12"><circle cx="6" cy="6" r="5.3" fill="none" stroke="#1d3c78"/><path d="M4 3.5l1 1-.6.8c.4.9 1 1.5 1.8 1.9l.8-.6 1 1-.7.9C5.5 8.3 3.7 6.5 3.3 4.3z" fill="#1d3c78"/></svg>(847) 555-0187</li>
      <li><svg viewBox="0 0 12 12"><circle cx="6" cy="6" r="5.3" fill="none" stroke="#1d3c78"/><rect x="3.5" y="3" width="5" height="6" rx=".6" fill="none" stroke="#1d3c78"/></svg>(847) 555-0163</li>
      <li><svg viewBox="0 0 12 12"><circle cx="6" cy="6" r="5.3" fill="none" stroke="#1d3c78"/><rect x="3" y="4" width="6" height="4" fill="none" stroke="#1d3c78" stroke-width=".8"/><path d="M3 4l3 2.2L9 4" fill="none" stroke="#1d3c78" stroke-width=".8"/></svg>fbarsow@curavista.us</li>
    </ul>
    <div class="web">www.curavista.us</div>
  </section>
</body>
</html>
```